Collagen Tub Packaging Design for a New Brand

PLEASE DON'T SEND ANY NEW DESIGNS WE JUST HAVE TO DECIDE WITH MY PARTNERS THANKS A LOT.
I've created a very detailed document & design examples of what we like in certain designs and what we don't.

There are 3 documents:
1- Brief for the Design (please read it before designing)
2- Brand Design Examples that we like (and why we like them)
3- Die cut for the packaging design. This will be it's dimensions.

We are NOT looking for someone to micro-manage. In contrast, we want someone to help us express our ideas better with their design. Nothing I say in these briefs are there to limit the creativity of the designer, because if we knew exactly what we wanted we would do it ourselves but we trust the designer's expertise in this packaging design.

In short: We want our brand to feel premium, high-quality & trust worthy with it's design not feeling very busy or bloated. We don't have a logo source file, but you'll get the idea of what we want when you see it).

Let me know if you have any further questions, will answer each question real fast.

Thanks.

Target Market(s)

Pretty much everyone above 25+ in Turkey because nearly all of them are using are collagens so our audience is wild.

Industry/Entity Type

Collagen - Health, Wellness & Supplements

Font styles to use
Serif
Sans Serif

Colors

Designer to choose colors to be used in the design.

Requirements
Must have
• Our design should be distinct, a design style which everyone can identify from 10 meters away if they know the product. This is a MUST have for us. It's up to designer to achieve it. This can be just a simple color palette aswell.
Should not have
• It shouldn't feel bloated and very busy. Please avoid very detailed icons (as a rule of thumb, if you can make it work great)

```html
<!DOCTYPE html>
<html lang="en">
<head>
<meta charset="UTF-8">
<title>Solvera Collagen Peptides – Tub Label</title>
<link rel="stylesheet" href="https://fonts.googleapis.com/css2?family=Open+Sans:wght@400;600;700&family=Oswald:wght@400;500&family=Cabin:wght@500;600&display=swap">
<style>
  :root {
    --page-bg: #f7f7f7;
    --royal: #1f33c0;
    --royal-deep: #1626a0;
    --navy: #1a2878;
    --sweep: #9fb0f0;
    --silver-light: #f4f4f6;
    --silver-mid: #c9cbd0;
    --silver-dark: #9a9ca2;
    --ink-blue: #1d3ac4;
    --body-ink: #2a2a2a;
    --white: #ffffff;
  }
  * { margin: 0; padding: 0; box-sizing: border-box; }
  html, body { width: 1200px; height: 982px; overflow: hidden; background: var(--page-bg); }
  body { position: relative; font-family: "Open Sans", sans-serif; }

  .label {
    position: absolute; left: 40px; top: 280px; width: 1120px; height: 420px;
    overflow: hidden; background: var(--white);
    box-shadow: 0 2px 10px rgba(0,0,0,0.08);
  }

  /* side panels */
  .info-panel {
    position: absolute; left: 0; top: 0; width: 220px; height: 420px;
    background: linear-gradient(90deg, #ffffff 0%, #f1f1f3 100%);
    padding: 34px 14px 0 16px;
  }
  .info-panel p {
    font-size: 7.6px; line-height: 1.62; color: var(--body-ink);
    text-align: justify; margin-bottom: 14px;
  }
  .info-panel p + p { padding-left: 12px; }

  .benefit-panel {
    position: absolute; left: 220px; top: 0; width: 140px; height: 420px;
    background: linear-gradient(90deg, #e4e5e8 0%, #ffffff 45%, #f3f3f5 100%);
    display: flex; flex-direction: column; align-items: center; padding-top: 92px;
  }
  .benefit {
    font-family: "Oswald", sans-serif; font-weight: 500; font-size: 19px;
    letter-spacing: 1.5px; color: var(--ink-blue);
  }
  .benefit-rule { width: 24px; height: 2px; background: var(--ink-blue); margin: 9px 0 12px; }

  /* front */
  .front-art { position: absolute; left: 360px; top: 0; width: 760px; height: 345px; }

  .brand { position: absolute; left: 430px; top: 38px; display: flex; align-items: center; gap: 10px; }
  .brand-dot { width: 14px; height: 14px; border-radius: 50%; background: var(--white); }
  .brand-name { font-family: "Open Sans", sans-serif; font-weight: 600; font-size: 38px; color: var(--white); letter-spacing: 1px; }
  .tagline { position: absolute; left: 482px; top: 90px; font-size: 12px; color: var(--white); letter-spacing: 0.5px; }

  .product { position: absolute; left: 420px; top: 178px; color: var(--white); }
  .product-kicker { font-family: "Cabin", sans-serif; font-weight: 500; font-size: 15px; opacity: 0.9; }
  .product-name { font-family: "Cabin", sans-serif; font-weight: 500; font-size: 58px; line-height: 0.95; letter-spacing: 1px; }
  .product-sub { font-family: "Open Sans", sans-serif; font-weight: 700; font-size: 17px; text-align: right; letter-spacing: 0.5px; margin-top: 2px; }

  .facts { position: absolute; left: 414px; top: 292px; display: flex; gap: 14px; color: var(--white); }
  .fact { display: flex; flex-direction: column; align-items: center; }
  .fact-value { font-family: "Oswald", sans-serif; font-size: 24px; line-height: 1; }
  .fact-value small { font-size: 14px; margin-left: 1px; }
  .fact-label { font-size: 7px; letter-spacing: 0.6px; margin-top: 3px; }

  .back-copy {
    position: absolute; left: 880px; top: 72px; width: 200px;
    font-size: 7.6px; line-height: 1.62; color: var(--white); text-align: justify;
  }

  /* bands */
  .silver-band {
    position: absolute; left: 0; top: 345px; width: 1120px; height: 45px;
    background: linear-gradient(90deg, var(--silver-dark) 0%, var(--silver-mid) 15%, var(--silver-light) 32%, #ffffff 55%, var(--silver-mid) 85%, var(--silver-dark) 100%);
  }
  .claim {
    position: absolute; left: 420px; top: 351px; font-size: 13px; line-height: 1.25;
    color: var(--ink-blue); font-weight: 600;
  }
  .base-band {
    position: absolute; left: 360px; top: 390px; width: 760px; height: 30px;
    background: linear-gradient(90deg, var(--royal-deep) 0%, var(--royal) 60%, var(--sweep) 68%, var(--navy) 80%);
  }
  .base-text {
    position: absolute; left: 414px; top: 393px; font-family: "Oswald", sans-serif;
    font-size: 16px; letter-spacing: 4px; color: var(--white);
  }
</style>
</head>
<body>
  <main class="label" aria-label="Solvera hydrolyzed collagen peptides tub label">
    <section class="info-panel">
      <p>Our hydrolyzed collagen peptides dissolve easily in water, coffee or smoothies. Mix one scoop into your favourite drink each morning. Made from carefully selected sources and tested for purity, every serving supports a daily routine of care for hair, skin, nails and joints. Store in a cool, dry place and keep the lid closed after use.</p>
      <p>Directions: add one scoop (12 g) to 250 ml of liquid and stir well. Do not exceed the recommended daily dose. Food supplements should not replace a varied diet. Keep out of reach of children.</p>
    </section>

    <section class="benefit-panel">
      <span class="benefit">HAIR</span><span class="benefit-rule"></span>
      <span class="benefit">SKIN</span><span class="benefit-rule"></span>
      <span class="benefit">NAILS</span><span class="benefit-rule"></span>
      <span class="benefit">JOINTS</span>
    </section>

    <svg class="front-art" viewBox="0 0 760 345" preserveAspectRatio="none" aria-hidden="true">
      <defs>
        <linearGradient id="front-fill" x1="0" y1="0" x2="1" y2="1">
          <stop offset="0" stop-color="#1a2bb0"/>
          <stop offset="0.6" stop-color="#2338c4"/>
          <stop offset="1" stop-color="#3047d2"/>
        </linearGradient>
        <linearGradient id="sweep-fill" x1="0" y1="0" x2="0" y2="1">
          <stop offset="0" stop-color="#c3cdf6"/>
          <stop offset="1" stop-color="#6f84e2"/>
        </linearGradient>
        <linearGradient id="back-fill" x1="0" y1="0" x2="1" y2="0">
          <stop offset="0" stop-color="#2a3cb0"/>
          <stop offset="1" stop-color="#19266e"/>
        </linearGradient>
      </defs>
      <rect width="760" height="345" fill="url(#back-fill)"/>
      <path d="M0 0 H470 C560 70 570 240 470 345 H0 Z" fill="url(#front-fill)"/>
      <path d="M470 0 H520 C610 80 610 250 505 345 H470 C570 240 560 70 470 0 Z" fill="url(#sweep-fill)" opacity="0.85"/>
    </svg>

    <div class="brand"><span class="brand-dot"></span><span class="brand-name">Solvera</span></div>
    <div class="tagline">Daha iyisi</div>

    <div class="product">
      <div class="product-kicker">hydrolyzed</div>
      <div class="product-name">COLLAGEN</div>
      <div class="product-sub">PEPTIDES</div>
    </div>

    <div class="facts">
      <div class="fact"><span class="fact-value">0<small>G</small></span><span class="fact-label">SUGAR</span></div>
      <div class="fact"><span class="fact-value">0<small>G</small></span><span class="fact-label">CARBS</span></div>
      <div class="fact"><span class="fact-value">0<small>G</small></span><span class="fact-label">FAT</span></div>
      <div class="fact"><span class="fact-value">11<small>G</small></span><span class="fact-label">PROTEIN</span></div>
      <div class="fact"><span class="fact-value">12<small>G</small></span><span class="fact-label">COLLAGEN</span></div>
    </div>

    <p class="back-copy">Ingredients: hydrolyzed bovine collagen peptides, acerola extract (natural vitamin C), silicium, probiotic cultures. Free from added sugar, gluten and artificial colours. Consult your doctor if you are pregnant, nursing or taking medication. Best before: see bottom of tub.</p>

    <div class="silver-band"></div>
    <p class="claim">With natural Vitamin C from acerola,<br>silicium and probiotics</p>
    <div class="base-band"></div>
    <span class="base-text">DIETARY SUPPLEMENT</span>
  </main>
</body>
</html>
```